Redesign Of Current Landing Page

I need to redesign this landing page https://www.bluewillowpromos.example/?page=landing&landing=23 (Please do not opt in because when you do it will show you the home page. Please clear your cookies before going to this url above to view the 1 page landing page.)

Please use my updated website as a reference for colors and logo.
http://sitecraftorly.example/dh/bwpg/index.html

I would like the call to action to be a button that opens into a lead form...

Button would be "Download Samples"

Target Market(s)

small business owners

Industry/Entity Type

Marketing

Number of Pages Required

1 page

Colors

Designer to choose colors to be used in the design.

Requirements
Must have
• must be full responsive on all devices
Nice to have
• must have a legitimate professional apeal to it
Should not have
• open

```html
<!DOCTYPE html>
<html lang="en">
<head>
<meta charset="utf-8">
<title>Blue Willow Promos – Attract More Customers</title>
<link href="https://fonts.googleapis.com/css2?family=Lato:wght@300;400;700;900&display=swap" rel="stylesheet">
<style>
  :root {
    --ink: #1a1a1a;
    --page: #e2e2e2;
    --text: #3a3a3a;
    --red: #e8302f;
    --blue: #1a74bf;
    --yellow: #f6b50f;
    --white: #ffffff;
    --icon: #3c3c3c;
  }
  * { box-sizing: border-box; margin: 0; padding: 0; }
  html, body { width: 1200px; height: 2620px; overflow: hidden; }
  body {
    position: relative;
    background: var(--page);
    font-family: "Lato", Arial, sans-serif;
    color: var(--text);
  }
  .site-header {
    position: absolute; left: 0; top: 0; width: 1200px; height: 128px;
    background: var(--ink);
  }
  .brand {
    position: absolute; left: 101px; top: 44px;
    display: flex; align-items: center; gap: 14px;
  }
  .brand-mark { width: 38px; height: 38px; background: var(--blue); }
  .brand-name {
    color: var(--blue); font-weight: 700; font-size: 30px; letter-spacing: 2px;
  }
  .hero {
    position: absolute; left: 0; top: 128px; width: 1200px; height: 623px;
    background: linear-gradient(100deg, #2b3a44 0%, #56707d 35%, #8da2ab 55%, #6b7b83 75%, #3b3a36 100%);
  }
  .hero-title {
    position: absolute; left: 100px; top: 180px;
    color: var(--white); font-weight: 700; font-size: 46px; line-height: 50px;
    letter-spacing: 4px; text-transform: uppercase;
  }
  .hero-sub {
    position: absolute; left: 100px; top: 290px;
    color: var(--white); font-size: 21px; line-height: 29px; letter-spacing: 2px;
    text-transform: uppercase;
  }
  .form-bar {
    position: absolute; left: 100px; top: 695px; width: 1001px; height: 56px;
    background: rgba(26,26,26,0.85);
    color: var(--white); font-weight: 700; font-size: 22px; letter-spacing: 1px;
    padding: 14px 0 0 57px;
  }
  .lead-form {
    position: absolute; left: 100px; top: 751px; width: 1001px; height: 166px;
    background: var(--blue); color: var(--white);
  }
  .lead-intro {
    position: absolute; left: 59px; top: 16px; width: 820px;
    font-size: 22px; line-height: 24px; letter-spacing: 1px;
  }
  .field {
    position: absolute; top: 81px; width: 171px; height: 38px;
    border: 1.5px solid #cfe2f3; color: var(--white);
    font-size: 15px; font-weight: 700; letter-spacing: 1px; padding: 11px 0 0 14px;
  }
  .field-name { left: 61px; }
  .field-email { left: 276px; }
  .field-phone { left: 489px; }
  .cta {
    position: absolute; left: 684px; top: 81px; width: 259px; height: 38px;
    background: var(--yellow); color: var(--ink);
    font-size: 17px; font-weight: 900; letter-spacing: 2px; text-align: center; padding-top: 9px;
  }
  .mandatory {
    position: absolute; left: 61px; top: 133px;
    font-size: 14px; font-style: italic; font-weight: 700;
  }
  .section { position: absolute; left: 161px; width: 882px; }
  .section h2 {
    color: var(--red); font-weight: 300; font-size: 44px; letter-spacing: 2px;
    line-height: 50px; text-transform: uppercase;
  }
  .section p {
    font-size: 21.5px; line-height: 30.5px; letter-spacing: 0.8px; text-align: justify;
    font-weight: 400;
  }
  .imagine { top: 968px; }
  .how { top: 1297px; }
  .how p { line-height: 38.5px; font-weight: 300; color: #333; }
  .testimonial {
    position: absolute; left: 145px; top: 1710px; width: 860px;
  }
  .quote-mark {
    position: absolute; left: 0; top: -10px; font-size: 90px; font-weight: 900;
    color: var(--ink); line-height: 90px;
  }
  .quote-text {
    margin-left: 56px; font-size: 18.5px; line-height: 33px; letter-spacing: 0.4px;
    font-weight: 400;
  }
  .quote-author {
    text-align: right; font-size: 18px; font-weight: 700; line-height: 30px;
    margin-top: 8px; margin-right: -1px; color: var(--ink);
  }
  .benefits-title {
    position: absolute; left: 161px; top: 2045px;
    color: var(--red); font-weight: 700; font-size: 33px; letter-spacing: 2px;
  }
  .benefit {
    position: absolute; width: 230px; margin-left: -115px; text-align: center;
    font-size: 18px; line-height: 24px; font-weight: 400; color: #444;
  }
  .benefit svg { display: block; margin: 0 auto 36px; fill: var(--icon); }
  .site-footer {
    position: absolute; left: 0; top: 2563px; width: 1200px; height: 57px;
    background: var(--ink); color: var(--white);
    font-size: 18px; letter-spacing: 0.5px; text-align: center; padding-top: 17px;
  }
</style>
</head>
<body>
  <header class="site-header">
    <div class="brand">
      <span class="brand-mark"></span>
      <span class="brand-name">BLUE WILLOW PROMOS</span>
    </div>
  </header>

  <section class="hero" role="img" aria-label="Photo of a smiling businessman in glasses leaning back relaxed at his desk in a bright office">
    <h1 class="hero-title">Attract More<br>Customers</h1>
    <p class="hero-sub">Who spend more money with<br>your business more often!</p>
  </section>

  <div class="form-bar">ENTER YOUR INFO</div>
  <form class="lead-form">
    <p class="lead-intro">To be fowarded to our website for all the details and to receive samples in your email!</p>
    <div class="field field-name">Name*</div>
    <div class="field field-email">Email*</div>
    <div class="field field-phone">Phone*</div>
    <div class="cta">DOWNLOAD SAMPLES</div>
    <p class="mandatory">*mandatory fields</p>
  </form>

  <section class="section imagine">
    <h2>Imagine</h2>
    <p>being able to create exciting give away promotions that will boost your sales without ever having to worry about cost.<br>
    Blue Willow Promotions Group, Inc. provides high-perceived value promotional incentives to businesses that want to advertise an exciting Give Away that will instantly attract more customers from your existing advertising efforts.<br>
    Your business can give away incentive certificates that are redeemable for luxury hotel &amp; resort stays with airfare included, cruises, cash for gas, groceries, dining and even electronic goods.</p>
  </section>

  <section class="section how">
    <h2>How can we do it?</h2>
    <p>We help fill empty rooms for thousands of hotels and resorts in hundreds of destinations around the world as well as the major cruise lines. Hotels and resorts are rarely full so when we place someone in their empty rooms, they end up making it up when travelers spend money on room service, spa services, eat at their in-house restaurants, casino and take advantage of other amenities that drive revenue.<br>
    We also help over 18,000 restaurants, electronic manufacturers, the major gas companies and top grocery chains in the U.S and Canada increase brand awareness as well as increase customer loyalty.</p>
  </section>

  <blockquote class="testimonial">
    <span class="quote-mark">&ldquo;</span>
    <p class="quote-text">I began using your incentives two years ago to boost lead generation efforts.<br>
    I have experienced a 63% increase in lead captures. And, even more importantly, my sales have increased as well. The ability to offer unlimited certificates and not having to pay for each certificate I give away is perhaps the best feature of the program, but having the flexibility to email or print certificates for my customers is also wonderful. I even use your html banners to automate my promotions right on my website!,</p>
    <p class="quote-author">Mark T.<br>Millersville, TN</p>
  </blockquote>

  <h2 class="benefits-title">HOW CAN WE DO IT?</h2>

  <div class="benefit" style="left:253px; top:2132px;">
    <svg width="66" height="78" viewBox="0 0 66 78"><rect x="4" y="56" width="12" height="22"/><rect x="22" y="44" width="12" height="34"/><rect x="40" y="30" width="12" height="48"/><path d="M2 40 L44 10 L40 5 L60 2 L54 20 L50 15 L6 46 Z"/></svg>
    Increase Responses<br>From Your Existing Ads
  </div>
  <div class="benefit" style="left:475px; top:2132px;">
    <svg width="80" height="78" viewBox="0 0 80 78"><path d="M34 4h12l2 9 7 3 8-5 8 8-5 8 3 7 9 2v12l-9 2-3 7 5 8-8 8-8-5-7 3-2 9H34l-2-9-7-3-8 5-8-8 5-8-3-7-9-2V35l9-2 3-7-5-8 8-8 8 5 7-3z M40 27a13 13 0 1 0 0.1 0z"/><path d="M48 50 L70 72 L64 78 L42 56 Z"/></svg>
    #1 Sales Closing Tool -<br>Gift w/ Purchase
  </div>
  <div class="benefit" style="left:711px; top:2132px;">
    <svg width="80" height="78" viewBox="0 0 80 78"><path d="M40 14 L49 38 L75 38 L54 53 L62 78 L40 62 L18 78 L26 53 L5 38 L31 38 Z"/><path d="M14 6l2 5 5 0-4 3 2 5-5-3-5 3 2-5-4-3 5 0z M66 6l2 5 5 0-4 3 2 5-5-3-5 3 2-5-4-3 5 0z M40 0l2 5 5 0-4 3 2 5-5-3-5 3 2-5-4-3 5 0z"/></svg>
    Build Brand Awareness<br>and Trust
  </div>
  <div class="benefit" style="left:949px; top:2132px;">
    <svg width="80" height="78" viewBox="0 0 80 78"><circle cx="16" cy="9" r="8"/><circle cx="58" cy="9" r="8"/><path d="M6 20h20l12 14-4 4-10-8v48h-7V54h-4v24H6z"/><path d="M68 20H48L38 32l4 4 8-7v49h7V54h4v24h7z"/><rect x="56" y="50" width="22" height="16"/></svg>
    Build Brand Awareness<br>and Trust
  </div>
  <div class="benefit" style="left:475px; top:2330px;">
    <svg width="80" height="66" viewBox="0 0 80 66"><path d="M50 0 L80 16 L50 32 L50 22 L4 22 L4 10 L50 10 Z"/><path d="M30 34 L0 50 L30 66 L30 56 L76 56 L76 44 L30 44 Z"/></svg>
    Boost Repeat and Referral<br>Business-
  </div>
  <div class="benefit" style="left:711px; top:2330px;">
    <svg width="70" height="66" viewBox="0 0 70 66"><path fill-rule="evenodd" d="M29 0h12l2 8 7 3 7-4 8 8-4 7 3 7 6 2v12l-6 2-3 7 4 7-8 8-7-4-7 3-2 8H29l-2-8-7-3-7 4-8-8 4-7-3-7-6-2V27l6-2 3-7-4-7 8-8 7 4 7-3z M35 13a20 20 0 1 0 .1 0z"/><text x="35" y="42" font-family="Lato, sans-serif" font-weight="900" font-size="24" text-anchor="middle">$</text></svg>
    Improve Retention<br>Rates
  </div>

  <footer class="site-footer">© 2017 Blue Willow Promotions Group, Inc. - All Rights Reserved</footer>
</body>
</html>
```